PennantVoyage

1. Can you describe what your company does?

Please find enclosed documents for your reference about our business doing.

2. Who are your target customers for the website?

Company Positioning: A comprehensive supplier of premier international sports travel and high-end event services.
Core Advantage: Exclusive international partnership resources and an Official Ticketing Assurance System.
Service Standard: One-Stop, High-Quality Service Solutions based on the "An once-in-a-lifetime experience" philosophy.

Our target customers for the website:
Mid-to-High-end Sports Enthusiasts
Corporate Clients
Sports Associations
Please kindly find enclosed for more details about our target customers, I think it's very important to make it clear to you.

3. Do you have an existing domain name / website address?

Yes, I have. I just applied for this new domain and it's totally a new website. www.pennantvoyage.com

4. In addition to a Home Page, which other pages / sections would you like your website to have:
About Us
Contact Us , Office / Mailing Address
Sports Travel Products( Bucket Lists) : Vessel Meet, Amber Round, Heliads, Football, KLQ, Golf, Skiing, Hiking,Galas
Reviews/ Unforgettable Moments
FAQs
Any other page / section you would like: Here is the website for your reference, www.laneweaver.com
For each of the pages / sections you’d like to have, please provide the text (and images, if available) you would like to include.
Please recommend 2-3 templates to me, and let me know what kind of text I will provide to every web pages.

5. Which of the below are features and functionalities your website will need:
Image Gallery
Videos
Contact Form
Maps
FAQs
6. Please provide the URLs for the social media profiles you'd like to link to the website.

Do you know Quiet Blue Ledger?

Please let me know anything you need, thank you very much!

Have a good day!

Target Market(s)

Travel for the world-wide sports games and make an once-in-a-lifetime experience

Industry/Entity Type

sports and travel industry

Coding

Coded - Design and coding required

Number of Pages Required

5+ page

Requirements
Must have
• our logo
Nice to have
• On the homepage, I’d like a banner-style section to prominently showcase the latest products.

```html
<!DOCTYPE html>
<html lang="en">
<head>
<meta charset="utf-8">
<title>PennantVoyage — Sports Travel</title>
<link href="https://fonts.googleapis.com/css2?family=Montserrat:wght@400;500;600;700;800&display=swap" rel="stylesheet">
<style>
:root{
  --orange:#f4590f;
  --orange-deep:#e04a06;
  --ink:#1f1f1f;
  --ink-dark:#151515;
  --black:#0a0a0a;
  --white:#ffffff;
  --muted:#d8d8d8;
}
*{box-sizing:border-box;margin:0;padding:0}
html,body{width:1200px;height:4979px;overflow:hidden;background:var(--ink)}
body{font-family:'Montserrat',sans-serif;color:var(--white);position:relative}
.abs{position:absolute}
.fill{position:absolute;display:block}

/* header */
.site-header{left:0;top:0;width:1200px;height:78px;background:var(--black)}
.brand{font-weight:800;color:var(--orange);font-size:22px;letter-spacing:.3px;line-height:1;white-space:nowrap}
.nav a{position:absolute;top:31px;font-size:12px;font-weight:500;color:var(--white);text-decoration:none}
.nav a.active{color:var(--orange)}
.btn{position:absolute;background:var(--orange);color:var(--white);font-weight:700;font-size:13px;display:flex;align-items:center;justify-content:center;border-radius:3px;text-transform:uppercase}

/* hero */
.hero{left:0;top:78px;width:1200px;height:517px;background:
  radial-gradient(ellipse 320px 260px at 860px 330px,rgba(40,90,110,.55),rgba(0,0,0,0)),
  radial-gradient(ellipse 500px 200px at 900px 120px,rgba(170,180,175,.6),rgba(0,0,0,0)),
  linear-gradient(180deg,#7d8a80 0%,#5e7a45 35%,#6e6244 70%,#3a3024 100%)}
.hero-shade{left:0;top:78px;width:760px;height:517px;background:linear-gradient(90deg,rgba(0,0,0,.82),rgba(0,0,0,.45) 60%,rgba(0,0,0,0))}
.hero-title{left:117px;top:146px;font-size:33px;font-weight:600;line-height:44.5px;text-transform:uppercase}
.hero-title .accent{color:var(--orange)}
.hero-copy{left:122px;top:337px;font-size:15px;line-height:25px;width:480px}

/* section headings */
.heading{font-size:38px;font-weight:500;text-transform:uppercase;line-height:1}
.heading .accent{color:var(--orange)}
.rule{position:absolute;height:4px;width:66px;background:var(--orange)}
.centered{left:0;width:1200px;text-align:center}

/* about */
.about-photo{border-radius:6px}
.about-copy{left:633px;top:800px;width:392px;font-size:13px;line-height:24px;text-align:justify;color:var(--muted)}
.sub{left:633px;top:934px;font-size:18px;font-weight:600}
.values{left:636px;top:975px;list-style:none}
.values li{font-size:15px;font-weight:500;height:28px;display:flex;align-items:center;gap:10px}

/* products */
.products-band{left:0;top:1240px;width:1200px;height:325px;background:linear-gradient(180deg,#121212,#1a1a1a)}
.card{border-radius:6px;overflow:hidden}
.card-title{font-size:19px;font-weight:700}
.card-text{font-size:13px;line-height:27px;color:#eee}
.circle-arrow{position:absolute}

/* location */
.location{left:0;top:2674px;width:1200px;height:769px;background:var(--orange)}
.map{left:255px;top:2877px;width:821px;height:462px;border-radius:6px;background:
  radial-gradient(ellipse 200px 160px at 700px 280px,rgba(110,170,100,.8),rgba(0,0,0,0)),
  radial-gradient(ellipse 260px 200px at 250px 220px,rgba(225,225,215,.9),rgba(0,0,0,0)),
  linear-gradient(135deg,#dfe3de 0%,#d4ddd0 45%,#a8cc9e 75%,#b7d4ae 100%)}
.places{left:114px;top:2964px;width:313px;height:303px;background:rgba(255,255,255,.93);border-radius:10px}
.place{position:absolute;left:22px;font-size:17px;font-weight:500;color:#111;display:flex;align-items:center;gap:8px;text-transform:uppercase}
.place.active{left:10px;width:293px;height:45px;top:9px;background:var(--orange);color:var(--white);border-radius:6px;padding-left:12px}

/* faq */
.faq-item{left:213px;width:773px;height:46px;background:#0b0b0b;border-radius:4px;display:flex;align-items:center;justify-content:space-between;padding:0 16px;font-size:13.5px;font-weight:600}
.faq-item .plus{font-size:22px;font-weight:600}

/* contact */
.contact-photo{left:133px;top:4055px;width:472px;height:441px;border-radius:30px;background:
  radial-gradient(ellipse 90px 170px at 120px 300px,rgba(210,110,40,.85),rgba(0,0,0,0)),
  radial-gradient(ellipse 90px 170px at 330px 310px,rgba(60,60,70,.8),rgba(0,0,0,0)),
  linear-gradient(180deg,#c4d4d8 0%,#8ea8b0 35%,#e6ecee 60%,#6a7884 100%)}
.form-panel{left:514px;top:4165px;width:566px;height:410px;border-radius:30px;background:linear-gradient(135deg,#f05a0a,#d84406)}
.field{position:absolute;background:var(--white);border-radius:5px;color:#333;font-size:11px;padding:14px 0 0 17px}
.send{position:absolute;background:var(--black);color:var(--white);border-radius:5px;font-weight:700;font-size:14px;display:flex;align-items:center;justify-content:center}

/* footer */
.site-footer{left:0;top:4672px;width:1200px;height:307px;background:var(--black)}
.foot-nav a,.foot-nav span{position:absolute;top:4842px;font-size:13px;color:var(--white);text-decoration:none}
.foot-rule{left:120px;top:4901px;width:960px;height:2px;background:#cfcfcf}
.copyright{top:4932px;font-size:12px;color:#ddd}
</style>
</head>
<body>

<!-- Header -->
<header class="abs site-header">
  <div class="abs brand" style="left:122px;top:28px">PENNANTVOYAGE</div>
  <nav class="nav">
    <a class="active" href="#" style="left:396px">HOME</a>
    <a href="#" style="left:477px">ABOUT US</a>
    <a href="#" style="left:576px">PRODUCTS</a>
    <a href="#" style="left:680px">FAQS</a>
    <a href="#" style="left:752px">CONTACT US</a>
  </nav>
  <div class="btn" style="left:873px;top:19px;width:205px;height:43px;font-size:14px">Start Your Journey</div>
</header>

<!-- Hero -->
<section>
  <div class="fill hero" role="img" aria-label="Hikers with backpacks and trekking poles walking a mountain trail through a green valley"></div>
  <div class="fill hero-shade"></div>
  <h1 class="abs hero-title">Experience sports like<br><span class="accent">never before—</span><br>luxury, exclusivity,<br>unforgettable moments.</h1>
  <p class="abs hero-copy">Official ticketing, exclusive partnerships, and tailor-made travel packages for the world's greatest sporting events.</p>
  <div class="btn" style="left:120px;top:413px;width:164px;height:45px">Get Started</div>
  <svg class="abs" style="left:805px;top:258px" width="86" height="86" viewBox="0 0 86 86">
    <circle cx="43" cy="43" r="43" fill="#111"/>
    <path d="M33 25 L63 43 L33 61 Z" fill="#fff"/>
  </svg>
</section>

<!-- About -->
<section>
  <div class="fill about-photo" style="left:129px;top:701px;width:215px;height:207px;background:radial-gradient(ellipse 120px 60px at 110px 180px,rgba(70,130,80,.9),rgba(0,0,0,0)),linear-gradient(180deg,#2d4660,#6a8a90 55%,#3f6b4c)" role="img" aria-label="Tennis player standing on a court in a floodlit stadium"></div>
  <div class="fill about-photo" style="left:361px;top:717px;width:213px;height:206px;background:radial-gradient(ellipse 90px 80px at 110px 120px,rgba(120,100,80,.7),rgba(0,0,0,0)),linear-gradient(160deg,#e6eef2,#a4aca4 50%,#4a4c3c)" role="img" aria-label="Three golfers in caps laughing together on a course"></div>
  <div class="fill about-photo" style="left:129px;top:923px;width:215px;height:207px;background:radial-gradient(ellipse 70px 60px at 100px 100px,rgba(200,60,30,.85),rgba(0,0,0,0)),linear-gradient(160deg,#f2e6dc,#d8c8c0 45%,#e9eef2)" role="img" aria-label="Skier in a red jacket carving through fresh snow"></div>
  <div class="fill about-photo" style="left:361px;top:939px;width:213px;height:205px;background:linear-gradient(160deg,#7eb2e4,#3c7fc8 60%,#b9d4ee)" role="img" aria-label="Large ring sculpture against a blue sky"></div>

  <h2 class="abs heading" style="left:630px;top:713px">About <span class="accent">Us</span></h2>
  <div class="rule" style="left:633px;top:771px"></div>
  <p class="abs about-copy">Our company has been deeply rooted in the sports and high-end service sector for over a decade, with businesses covering High-end Conference Management and Planning, Sports Event Operation, and, at its core, Sports Travel services.</p>
  <h3 class="abs sub">Core Value and Competencies:</h3>
  <ul class="abs values">
    <li><svg width="12" height="10" viewBox="0 0 12 10"><path d="M1 1 L5 5 L1 9 M6 1 L10 5 L6 9" stroke="#f4590f" stroke-width="1.6" fill="none"/></svg>Professional Qualification</li>
    <li><svg width="12" height="10" viewBox="0 0 12 10"><path d="M1 1 L5 5 L1 9 M6 1 L10 5 L6 9" stroke="#f4590f" stroke-width="1.6" fill="none"/></svg>Resource Advantage</li>
    <li><svg width="12" height="10" viewBox="0 0 12 10"><path d="M1 1 L5 5 L1 9 M6 1 L10 5 L6 9" stroke="#f4590f" stroke-width="1.6" fill="none"/></svg>All-encompassing Service</li>
  </ul>
  <div class="btn" style="left:634px;top:1088px;width:172px;height:42px">Read More</div>
</section>

<!-- Products -->
<section>
  <div class="fill products-band"></div>
  <h2 class="abs heading centered" style="top:1324px">Our <span class="accent">Products</span></h2>
  <div class="rule" style="left:567px;top:1381px"></div>

  <div class="fill card" style="left:120px;top:1422px;width:456px;height:288px;background:radial-gradient(ellipse 60px 120px at 290px 140px,rgba(220,170,60,.85),rgba(0,0,0,0)),linear-gradient(180deg,#3a3c4a 0%,#6b5a48 45%,#a04a1a 100%)" role="img" aria-label="Golden trophy on a stage with confetti and stadium lights"></div>
  <div class="abs card-title" style="left:136px;top:1618px">Vessel Meet</div>
  <p class="abs card-text" style="left:136px;top:1644px;width:300px">Lorem Ipsum is simply dummy text of the printing and typesetting industry. Lorem</p>

  <div class="fill card" style="left:624px;top:1422px;width:456px;height:288px;background:radial-gradient(circle 28px at 330px 140px,rgba(210,220,70,.9),rgba(0,0,0,0)),linear-gradient(180deg,#2c5c7a 0%,#4a6878 40%,#a4502a 75%,#c2582a 100%)" role="img" aria-label="Close view of a player's shoe beside a tennis ball on a clay court"></div>
  <div class="abs card-title" style="left:640px;top:1618px">Amber Round</div>
  <p class="abs card-text" style="left:640px;top:1644px;width:300px">Lorem Ipsum is simply dummy text of the printing and typesetting industry. Lorem</p>

  <svg class="circle-arrow" style="left:34px;top:1518px" width="36" height="36" viewBox="0 0 36 36"><circle cx="18" cy="18" r="16" fill="none" stroke="#fff" stroke-width="2"/><path d="M26 18 H11 M17 12 L11 18 L17 24" stroke="#fff" stroke-width="2" fill="none"/></svg>
  <svg class="circle-arrow" style="left:1126px;top:1518px" width="36" height="36" viewBox="0 0 36 36"><circle cx="18" cy="18" r="16" fill="none" stroke="#fff" stroke-width="2"/><path d="M10 18 H25 M19 12 L25 18 L19 24" stroke="#fff" stroke-width="2" fill="none"/></svg>

  <div class="btn" style="left:514px;top:1766px;width:172px;height:42px">View More</div>
</section>

<!-- Gallery -->
<section>
  <h2 class="abs heading centered" style="top:1875px">Our <span class="accent">Gallery</span></h2>
  <div class="rule" style="left:567px;top:1934px"></div>
  <div class="fill" style="left:120px;top:1978px;width:303px;height:248px;background:radial-gradient(ellipse 90px 70px at 190px 110px,rgba(220,220,215,.7),rgba(0,0,0,0)),linear-gradient(135deg,#1d4f6e,#7a6a58 55%,#d07a3a)" role="img" aria-label="Tennis player lunging for a ball"></div>
  <div class="fill" style="left:448px;top:1978px;width:304px;height:248px;background:radial-gradient(ellipse 70px 80px at 160px 120px,rgba(225,205,40,.9),rgba(0,0,0,0)),linear-gradient(135deg,#c7d2d8,#7c9a6a 50%,#6a9a4a)" role="img" aria-label="Group of hikers on a green mountain path"></div>
  <div class="fill" style="left:777px;top:1978px;width:303px;height:248px;background:radial-gradient(ellipse 50px 60px at 180px 120px,rgba(210,160,40,.9),rgba(0,0,0,0)),linear-gradient(135deg,#3a2a1a,#1a1c24 55%,#6a4a1a)" role="img" aria-label="Person in a tuxedo holding a golden trophy at an evening gala"></div>
  <div class="fill" style="left:120px;top:2251px;width:303px;height:247px;background:radial-gradient(ellipse 70px 90px at 140px 150px,rgba(200,80,30,.85),rgba(0,0,0,0)),linear-gradient(180deg,#1c2a4a,#2a2a3a 55%,#4a2a1a)" role="img" aria-label="Basketball player facing the hoop in an arena"></div>
  <div class="fill" style="left:448px;top:2251px;width:304px;height:247px;background:radial-gradient(ellipse 80px 90px at 160px 90px,rgba(140,30,50,.9),rgba(0,0,0,0)),linear-gradient(180deg,#4a8a3a,#3a9a3a 55%,#3aa03a)" role="img" aria-label="Football players competing for the ball on grass"></div>
  <div class="fill" style="left:777px;top:2251px;width:303px;height:247px;background:radial-gradient(ellipse 60px 60px at 160px 90px,rgba(220,110,40,.9),rgba(0,0,0,0)),linear-gradient(135deg,#4a6a8a,#b8c8d8 50%,#eef2f6)" role="img" aria-label="Skier jumping over snowy mountain terrain"></div>
  <div class="btn" style="left:512px;top:2543px;width:174px;height:42px">View More</div>
</section>

<!-- Location -->
<section>
  <div class="fill location"></div>
  <h2 class="abs heading centered" style="top:2757px">Location We Serve</h2>
  <div class="rule" style="left:567px;top:2815px;background:#fff"></div>
  <div class="fill map" role="img" aria-label="Street map of the served city region with highways and parks"></div>
  <div class="fill places">
    <div class="place active"><svg width="14" height="18" viewBox="0 0 14 18"><path d="M7 1 C3.5 1 1 3.6 1 7 C1 11 7 17 7 17 C7 17 13 11 13 7 C13 3.6 10.5 1 7 1 Z" fill="none" stroke="#fff" stroke-width="2"/><circle cx="7" cy="7" r="2" fill="#fff"/></svg>Australia</div>
    <div class="place" style="top:68px"><svg width="14" height="18" viewBox="0 0 14 18"><path d="M7 1 C3.5 1 1 3.6 1 7 C1 11 7 17 7 17 C7 17 13 11 13 7 C13 3.6 10.5 1 7 1 Z" fill="none" stroke="#111" stroke-width="2"/><circle cx="7" cy="7" r="2" fill="#111"/></svg>Spain (Barcelona)</div>
    <div class="place" style="top:104px"><svg width="14" height="18" viewBox="0 0 14 18"><path d="M7 1 C3.5 1 1 3.6 1 7 C1 11 7 17 7 17 C7 17 13 11 13 7 C13 3.6 10.5 1 7 1 Z" fill="none" stroke="#111" stroke-width="2"/><circle cx="7" cy="7" r="2" fill="#111"/></svg>United Kingdom</div>
    <div class="place" style="top:140px"><svg width="14" height="18" viewBox="0 0 14 18"><path d="M7 1 C3.5 1 1 3.6 1 7 C1 11 7 17 7 17 C7 17 13 11 13 7 C13 3.6 10.5 1 7 1 Z" fill="none" stroke="#111" stroke-width="2"/><circle cx="7" cy="7" r="2" fill="#111"/></svg>USA Cities</div>
    <div class="place" style="top:176px"><svg width="14" height="18" viewBox="0 0 14 18"><path d="M7 1 C3.5 1 1 3.6 1 7 C1 11 7 17 7 17 C7 17 13 11 13 7 C13 3.6 10.5 1 7 1 Z" fill="none" stroke="#111" stroke-width="2"/><circle cx="7" cy="7" r="2" fill="#111"/></svg>Fannin</div>
    <div class="place" style="top:212px"><svg width="14" height="18" viewBox="0 0 14 18"><path d="M7 1 C3.5 1 1 3.6 1 7 C1 11 7 17 7 17 C7 17 13 11 13 7 C13 3.6 10.5 1 7 1 Z" fill="none" stroke="#111" stroke-width="2"/><circle cx="7" cy="7" r="2" fill="#111"/></svg>Japan</div>
    <div class="place" style="top:248px"><svg width="14" height="18" viewBox="0 0 14 18"><path d="M7 1 C3.5 1 1 3.6 1 7 C1 11 7 17 7 17 C7 17 13 11 13 7 C13 3.6 10.5 1 7 1 Z" fill="none" stroke="#111" stroke-width="2"/><circle cx="7" cy="7" r="2" fill="#111"/></svg>Brazil</div>
  </div>
</section>

<!-- FAQ -->
<section>
  <h2 class="abs heading centered" style="top:3537px">Frequently <span class="accent">Asked Questions</span></h2>
  <div class="rule" style="left:567px;top:3596px"></div>
  <div class="abs faq-item" style="top:3636px"><span>Lorem Ipsum is simply dummy text of the printing and typesetting industry</span><span class="plus">+</span></div>
  <div class="abs faq-item" style="top:3696px"><span>Lorem Ipsum is simply dummy text of the printing and typesetting industry</span><span class="plus">+</span></div>
  <div class="abs faq-item" style="top:3756px"><span>Lorem Ipsum is simply dummy text of the printing and typesetting industry</span><span class="plus">+</span></div>
  <div class="abs faq-item" style="top:3816px"><span>Lorem Ipsum is simply dummy text of the printing and typesetting industry</span><span class="plus">+</span></div>
  <div class="abs faq-item" style="top:3875px"><span>Lorem Ipsum is simply dummy text of the printing and typesetting industry</span><span class="plus">+</span></div>
  <div class="abs faq-item" style="top:3934px"><span>Lorem Ipsum is simply dummy text of the printing and typesetting industry</span><span class="plus">+</span></div>
</section>

<!-- Contact -->
<section>
  <div class="fill contact-photo" role="img" aria-label="Two skiers seen from behind looking out over snowy mountains"></div>
  <h2 class="abs heading" style="left:630px;top:4084px">Contact <span class="accent">Us</span></h2>
  <div class="fill form-panel"></div>
  <div class="field" style="left:537px;top:4221px;width:255px;height:47px">First Name</div>
  <div class="field" style="left:807px;top:4221px;width:256px;height:47px">Last Name</div>
  <div class="field" style="left:537px;top:4283px;width:255px;height:47px">Email Address</div>
  <div class="field" style="left:807px;top:4283px;width:256px;height:47px">Phone Number</div>
  <div class="field" style="left:537px;top:4345px;width:526px;height:105px">Your message</div>
  <div class="send" style="left:879px;top:4469px;width:178px;height:42px">SEND</div>
</section>

<!-- Footer -->
<footer>
  <div class="fill site-footer"></div>
  <div class="abs brand centered" style="top:4762px;font-size:26px">PENNANTVOYAGE</div>
  <nav class="foot-nav">
    <a href="#" style="left:305px">HOME</a><span style="left:383px">|</span>
    <a href="#" style="left:428px">ABOUT US</a><span style="left:531px">|</span>
    <a href="#" style="left:576px">PRODUCT</a><span style="left:682px">|</span>
    <a href="#" style="left:721px">FAQ</a><span style="left:787px">|</span>
    <a href="#" style="left:832px">CONTACT</a>
  </nav>
  <div class="fill foot-rule"></div>
  <p class="abs copyright centered">© 2025 PennantVoyage I All Rights Reserved</p>
</footer>

</body>
</html>
```